Expedition Cruise Sales Website for the Polar Regions (Antarctica & Arctic)

This will be a website for selling cruises.
This site should have a homepage, a ship page, destinations, and itineraries.
I have created a file specifying each page, and it is attached.
Pages:
1. Home
2. Cruise Lines
- 2.1 Ships
3. Destinations
- 3.1 Region - 3.2 Country - 3.3 City
4. Itineraries
- 4.1 Itinerary
5. Blog / Travel Tips 6. About Us
7. Contact
Please take a look on the attached pdf
Target Market(s)
Expedition Travelers
Coding
Coded - Design and coding required
Number of Pages Required
5+ page
Font styles to use
Look and feel
Each slider illustrates characteristics of the customer's brand and the style your logo design should communicate.

```html
<!DOCTYPE html>
<html lang="en">
<head>
<meta charset="utf-8">
<title>Polarvia – Expedition Cruises</title>
<link href="https://fonts.googleapis.com/css2?family=Nunito:wght@400;600;700;800;900&family=Open+Sans:wght@400;600;700&display=swap" rel="stylesheet">
<style>
:root{
  --blue:#3b72b3;
  --blue-dark:#2f5f9c;
  --hero-a:#1a49ad;
  --hero-b:#2b8fe3;
  --ink:#1c1c1c;
  --text:#555;
  --line:#dcdcdc;
  --star:#f26522;
  --footer:#1f1f1f;
  --white:#fff;
}
*{box-sizing:border-box;margin:0;padding:0}
html,body{width:1200px;height:3730px;overflow:hidden}
body{position:relative;background:var(--white);font-family:"Open Sans",sans-serif;color:var(--ink)}
.abs{position:absolute}
.btn{position:absolute;display:flex;align-items:center;justify-content:center;background:var(--blue);color:var(--white);border-radius:30px;font-family:"Nunito",sans-serif;font-weight:800;font-size:16px;letter-spacing:.3px}
.section-title{position:absolute;left:0;width:1200px;text-align:center;font-family:"Nunito",sans-serif;font-weight:600;font-size:42px;line-height:1}
.arrow{position:absolute;width:36px;height:36px;margin:-18px 0 0 -18px;border-radius:50%;border:1.5px solid #999;background:var(--white);display:flex;align-items:center;justify-content:center}
.arrow svg{width:14px;height:14px}

/* header */
.site-header{position:absolute;top:0;left:0;width:1200px;height:96px;background:var(--white);border-top:3px solid var(--blue);z-index:3}
.brand{position:absolute;left:140px;top:-36px;width:200px;height:200px;border-radius:50%;background:var(--white);z-index:4;display:flex;align-items:flex-end;justify-content:center;padding-bottom:74px}
.brand span{font-family:"Nunito",sans-serif;font-weight:800;font-size:31px;color:var(--blue)}
.main-nav{position:absolute;left:430px;top:36px;display:flex;gap:11px;font-family:"Open Sans",sans-serif;font-weight:700;font-size:12px;z-index:5}
.main-nav a{display:block;padding:7px 5px;color:var(--ink);text-decoration:none;line-height:15px}
.main-nav a.active{background:var(--blue);color:var(--white);border-radius:16px;padding:7px 11px}

/* hero */
.hero{position:absolute;top:96px;left:0;width:1200px;height:584px;background:linear-gradient(115deg,var(--hero-a) 0%,#2160c4 55%,var(--hero-b) 100%)}
.hero-title{position:absolute;top:120px;left:0;width:1200px;text-align:center;color:var(--white);font-family:"Nunito",sans-serif;font-weight:900;font-size:56px;line-height:66px;text-shadow:0 2px 6px rgba(0,0,0,.25)}
.play{position:absolute;left:574px;top:286px;width:52px;height:52px;border:3px solid var(--white);border-radius:50%}
.play svg{position:absolute;left:17px;top:13px}
.search-panel{position:absolute;left:145px;top:379px;width:912px;height:205px;background:#f7f9fc;border:6px solid var(--white);border-bottom:none}
.field{position:absolute;height:38px;background:var(--white);border:1px solid #e4e4e4;font-size:12px;color:#333;display:flex;align-items:center;padding-left:16px}
.field::after{content:"";position:absolute;right:14px;top:16px;border:5px solid transparent;border-top:6px solid #555}
.search-btn{left:392px;top:127px;width:126px;height:48px;font-size:17px}

/* offers */
.offer{position:absolute;top:850px;width:294px;height:376px;background:var(--white);border:1px solid #e2e2e2;box-shadow:0 1px 4px rgba(0,0,0,.06)}
.offer-img{position:absolute;left:2px;top:2px;width:288px;height:182px}
.heart{position:absolute;right:12px;top:172px;width:28px;height:28px;border-radius:50%;background:#111;display:flex;align-items:center;justify-content:center}
.heart.blue{background:var(--blue)}
.offer h3{position:absolute;left:18px;top:202px;font-family:"Open Sans",sans-serif;font-weight:700;font-size:16px}
.offer .meta{position:absolute;left:18px;top:234px;font-size:10.5px;color:#555}
.offer p{position:absolute;left:18px;top:255px;width:260px;font-size:12.5px;line-height:19px;color:#444}
.book{position:absolute;left:16px;top:311px;width:115px;height:39px;border:2px solid var(--blue);border-radius:22px;color:var(--blue);font-family:"Nunito",sans-serif;font-weight:800;font-size:13px;display:flex;align-items:center;justify-content:center}
.price{position:absolute;right:16px;top:315px;font-family:"Nunito",sans-serif;font-weight:800;font-size:15px;color:#222}
.price b{font-size:25px}

/* destinations */
.dest-band{position:absolute;left:0;top:1380px;width:1200px;height:430px}
.dest{position:absolute;border:2px solid var(--white);overflow:hidden}
.dest .photo{position:absolute;inset:0}
.dest .label{position:absolute;left:0;width:100%;text-align:center;color:var(--white);font-family:"Open Sans",sans-serif;font-weight:700;font-size:23px}
.plus{position:absolute;left:50%;margin-left:-16px;width:32px;height:32px;border-radius:50%;background:var(--white);color:var(--blue);font-size:22px;font-weight:700;display:flex;align-items:center;justify-content:center}

/* cruise lines */
.dots{position:absolute;background-image:radial-gradient(circle,#c9c9c9 2px,transparent 2.5px);background-size:10px 10px}
.cl-photo{position:absolute;border-radius:10px}
.partner{position:absolute;left:602px;top:2374px;width:162px;height:72px;border:2px solid #d6d6d6;border-radius:8px;display:flex;align-items:center;justify-content:center;font-family:"Open Sans",sans-serif;font-weight:700;font-size:16px;color:#222}
.stars{color:var(--star);letter-spacing:3px;font-size:17px}
.cl-text{position:absolute;left:604px;top:2478px;width:452px;font-size:14px;line-height:25.5px;color:#555;text-align:justify}

/* testimonials */
.review{position:absolute;top:3040px;width:265px}
.avatar{position:absolute;width:64px;height:64px;border-radius:50%;border:3px solid #eee}
.review .q{font-size:12px;line-height:22px;color:#555;padding-left:0}
.review .q i{color:#29a9e1;font-family:Georgia,serif;font-weight:700;font-size:18px;margin-right:8px}
.review .who{margin-top:18px;font-size:9.5px;font-weight:700;line-height:16px;color:#222}
.review .stars{margin-top:10px}

/* footer */
.site-footer{position:absolute;left:0;top:3366px;width:1200px;height:364px;background:var(--footer);color:var(--white)}
.site-footer h4{position:absolute;left:164px;top:47px;font-family:"Nunito",sans-serif;font-weight:700;font-size:20px}
.input{position:absolute;top:86px;height:48px;border-radius:26px;background:var(--white);color:#666;font-size:13px;display:flex;align-items:center;padding-left:33px}
.social{position:absolute;top:88px;width:48px;height:48px;border-radius:50%;border:2px solid var(--white);display:flex;align-items:center;justify-content:center;font-size:11px;font-weight:700}
.social.green{background:#25a244}
.foot-nav{position:absolute;left:0;top:230px;width:1200px;display:flex;justify-content:center;gap:30px;font-family:"Nunito",sans-serif;font-weight:800;font-size:17px}
.copy{position:absolute;left:0;top:287px;width:1200px;text-align:center;font-size:13.5px;color:#eee}
</style>
</head>
<body>

<header class="site-header">
  <nav class="main-nav">
    <a class="active">HOME</a><a>CRUISE LINES</a><a>SHIPS</a><a>ITINERARIES</a><a>DESTINATIONS</a><a>BLOG</a><a>ABOUT US</a><a>CONTACT</a>
  </nav>
</header>
<div class="brand"><span>Polarvia</span></div>

<section class="hero" role="img" aria-label="Large cruise ship sailing under a blue sky">
  <h1 class="hero-title">Explore the World<br>with a Smile</h1>
  <div class="play"><svg width="18" height="22" viewBox="0 0 18 22"><path d="M2 2 L16 11 L2 20 Z" fill="#fff"/></svg></div>
  <form class="search-panel">
    <div class="field" style="left:69px;top:17px;width:245px">Destinations</div>
    <div class="field" style="left:327px;top:17px;width:245px">Cruise Line</div>
    <div class="field" style="left:584px;top:17px;width:246px">Select Ship</div>
    <div class="field" style="left:69px;top:66px;width:245px">Any Day</div>
    <div class="field" style="left:327px;top:66px;width:156px">Days +/-</div>
    <div class="field" style="left:497px;top:66px;width:161px">March 2025</div>
    <div class="field" style="left:668px;top:66px;width:162px">2 Adults</div>
    <div class="btn search-btn">SEARCH</div>
  </form>
</section>

<h2 class="section-title" style="top:776px">FEATURED OFFERS</h2>
<div class="arrow" style="left:85px;top:1029px"><svg viewBox="0 0 14 14"><path d="M9 2 L4 7 L9 12" fill="none" stroke="#333" stroke-width="1.8"/></svg></div>
<div class="arrow" style="left:1113px;top:1029px"><svg viewBox="0 0 14 14"><path d="M5 2 L10 7 L5 12" fill="none" stroke="#333" stroke-width="1.8"/></svg></div>

<article class="offer" style="left:140px">
  <div class="offer-img" role="img" aria-label="Cruise ship on the open ocean" style="background:linear-gradient(180deg,#2e4f7a 0%,#1d3a66 60%,#2a4f80 100%)"></div>
  <div class="heart"><svg width="14" height="13" viewBox="0 0 14 13"><path d="M7 12 L1.5 6.5 A3 3 0 0 1 7 2.5 A3 3 0 0 1 12.5 6.5 Z" fill="#fff"/></svg></div>
  <h3>Best Antarctic Cruises</h3>
  <div class="meta">▦ 19 September 2018 &nbsp;|&nbsp; ◷ 7 Nights</div>
  <p>Neque porro quisquam est,qui dolorem ipsum quia dolor sit ame</p>
  <div class="book">BOOK NOW</div>
  <div class="price">from <b>£423</b>pp</div>
</article>
<article class="offer" style="left:452px">
  <div class="offer-img" role="img" aria-label="White cruise ship sailing under blue sky" style="background:linear-gradient(180deg,#2d6fbf 0%,#6ea3d8 55%,#1f4f86 100%)"></div>
  <div class="heart blue"><svg width="14" height="13" viewBox="0 0 14 13"><path d="M7 12 L1.5 6.5 A3 3 0 0 1 7 2.5 A3 3 0 0 1 12.5 6.5 Z" fill="#fff"/></svg></div>
  <h3>Top Galápagos Cruises</h3>
  <div class="meta">▦ 17 September 2018 &nbsp;|&nbsp; ◷ 7 Nights</div>
  <p>Neque porro quisquam est,qui dolorem ipsum quia dolor sit ame</p>
  <div class="book">BOOK NOW</div>
  <div class="price">from <b>£559</b>pp</div>
</article>
<article class="offer" style="left:763px">
  <div class="offer-img" role="img" aria-label="Cruise ship beside a green island in turquoise water" style="background:linear-gradient(180deg,#5fb6e6 0%,#2f8fb8 40%,#3aa6b8 100%)"></div>
  <div class="heart"><svg width="14" height="13" viewBox="0 0 14 13"><path d="M7 12 L1.5 6.5 A3 3 0 0 1 7 2.5 A3 3 0 0 1 12.5 6.5 Z" fill="#fff"/></svg></div>
  <h3>Last-Minute Deals</h3>
  <div class="meta">▦ 16th May 2018 &nbsp;|&nbsp; ◷ 7 Nights</div>
  <p>Neque porro qauisquam est,qui dolorem ipsum quia dolor sit ame</p>
  <div class="book">BOOK NOW</div>
  <div class="price">from <b>£599</b>pp</div>
</article>
<div class="btn" style="left:504px;top:1261px;width:191px;height:50px">VIEW MORE</div>

<svg class="dest-band" viewBox="0 0 1200 430" preserveAspectRatio="none">
  <path d="M0 154 Q600 -150 1200 154 L1200 430 L0 430 Z" fill="#3b72b3"/>
</svg>
<h2 class="section-title" style="top:1500px;color:#fff;font-weight:600">HIGHLIGHTED DESTINATIONS</h2>

<div class="dest" style="left:32px;top:1607px;width:278px;height:354px">
  <div class="photo" role="img" aria-label="Ancient Roman amphitheatre under a cloudy sky" style="background:linear-gradient(180deg,#7fa8d4 0%,#b58a5f 45%,#6e4b33 80%,#3d2d22 100%)"></div>
  <div class="label" style="top:285px">ITALY</div>
</div>
<div class="dest" style="left:326px;top:1669px;width:275px;height:350px">
  <div class="photo" role="img" aria-label="Paris skyline with the iron tower above green parks" style="background:linear-gradient(180deg,#8eb5da 0%,#7f93a6 45%,#4f6b3c 80%,#344a28 100%)"></div>
  <div class="label" style="top:256px">FRANCE</div>
  <div class="plus" style="top:292px">+</div>
</div>
<div class="dest" style="left:617px;top:1607px;width:276px;height:352px">
  <div class="photo" role="img" aria-label="Madrid street with domed building at sunset" style="background:linear-gradient(180deg,#4a6fb8 0%,#c77aa6 30%,#a46b4e 60%,#3d2f28 100%)"></div>
  <div class="label" style="top:285px">SPAIN</div>
</div>
<div class="dest" style="left:908px;top:1669px;width:276px;height:350px">
  <div class="photo" role="img" aria-label="New York skyline with tall skyscraper" style="background:linear-gradient(180deg,#5fb0e4 0%,#8ec0de 40%,#55606c 75%,#2d343c 100%)"></div>
  <div class="label" style="top:289px">UNITED STATES</div>
</div>
<div class="arrow" style="left:77px;top:1799px;border:none"><svg viewBox="0 0 14 14"><path d="M9 2 L4 7 L9 12" fill="none" stroke="#333" stroke-width="1.8"/></svg></div>
<div class="arrow" style="left:1122px;top:1799px;border:none"><svg viewBox="0 0 14 14"><path d="M5 2 L10 7 L5 12" fill="none" stroke="#333" stroke-width="1.8"/></svg></div>
<div class="btn" style="left:504px;top:2080px;width:191px;height:51px">VIEW MORE</div>

<div class="dots" style="left:91px;top:2186px;width:116px;height:116px"></div>
<div class="dots" style="left:350px;top:2762px;width:116px;height:43px"></div>
<div class="cl-photo" role="img" aria-label="Calm blue sea with small boats" style="left:14px;top:2485px;width:220px;height:304px;background:linear-gradient(180deg,#2e69b3 0%,#6f9fd2 45%,#2a5a9c 100%)"></div>
<div class="cl-photo" style="left:145px;top:2233px;width:383px;height:524px;background:#fff;border-radius:12px"></div>
<div class="cl-photo" role="img" aria-label="Cruise ship sailing through deep blue water, seen from above" style="left:159px;top:2247px;width:355px;height:497px;background:linear-gradient(180deg,#5a87bf 0%,#2e6fb5 30%,#1a5797 70%,#145089 100%)"></div>
<div class="arrow" style="left:139px;top:2495px;width:60px;height:60px;margin:-30px 0 0 -30px;border:none;box-shadow:0 1px 6px rgba(0,0,0,.2)"><svg viewBox="0 0 14 14"><path d="M9 2 L4 7 L9 12" fill="none" stroke="#222" stroke-width="2"/></svg></div>
<div class="arrow" style="left:514px;top:2495px;width:60px;height:60px;margin:-30px 0 0 -30px;border:none;box-shadow:0 1px 6px rgba(0,0,0,.2)"><svg viewBox="0 0 14 14"><path d="M5 2 L10 7 L5 12" fill="none" stroke="#222" stroke-width="2"/></svg></div>

<h2 class="abs" style="left:602px;top:2294px;font-family:'Nunito',sans-serif;font-weight:600;font-size:42px">CRUISE LINES</h2>
<div class="partner">Norvane Line</div>
<div class="abs" style="left:793px;top:2381px;font-family:'Nunito',sans-serif;font-weight:600;font-size:19px">Nemo enim ipsamv</div>
<div class="abs stars" style="left:793px;top:2408px">★★★★☆</div>
<p class="cl-text">Sed ut perspiciatis unde omnis iste natus error sit voluptatem accusantium doloremque laudantium, totam rem aperiam, eaque ipsa quae ab illo inventore veritatis et quasi architecto beatae vitae dicta sunt explicabo. Nemo enim ipsam voluptatem quia voluptas sit aspernatur aut odit aut fugit, sed quia cons</p>
<div class="btn" style="left:604px;top:2639px;width:191px;height:50px">READ MORE</div>

<div class="abs" style="left:132px;top:2862px;width:936px;height:2px;background:var(--line)"></div>

<h2 class="section-title" style="top:2944px">CUSTOMER TESTIMONIALS</h2>
<div class="arrow" style="left:85px;top:3073px"><svg viewBox="0 0 14 14"><path d="M9 2 L4 7 L9 12" fill="none" stroke="#333" stroke-width="1.8"/></svg></div>
<div class="arrow" style="left:1113px;top:3073px"><svg viewBox="0 0 14 14"><path d="M5 2 L10 7 L5 12" fill="none" stroke="#333" stroke-width="1.8"/></svg></div>

<div class="avatar" role="img" aria-label="Customer portrait" style="left:131px;top:3040px;background:linear-gradient(180deg,#d9b8a0,#a87a5e)"></div>
<div class="review" style="left:216px">
  <p class="q"><i>"</i>At vero eos et accusamus et iustodio dignissimos ducimus qui blanditiipraesnt ium voluptatum</p>
  <p class="who">MAREN HOLT<br>Financial Services Professional</p>
  <div class="stars">★★★★☆</div>
</div>
<div class="avatar" role="img" aria-label="Customer portrait" style="left:457px;top:3040px;background:linear-gradient(180deg,#cfcfcf,#6e6e6e)"></div>
<div class="review" style="left:543px">
  <p class="q"><i>"</i>At vero eos et accusamus et iustodio dignissimos ducimus qui blanditiipraesnt ium voluptatum deleniti atqu.</p>
  <p class="who">TOBIAS R. LINDQVIST<br>National Urban Fellow at the Houston</p>
  <div class="stars">★★★★☆</div>
</div>
<div class="avatar" role="img" aria-label="Customer portrait" style="left:781px;top:3040px;background:linear-gradient(180deg,#e0cbbb,#9d8574)"></div>
<div class="review" style="left:866px">
  <p class="q"><i>"</i>At vero eos et accusamus et iustodio dignissimos ducimus qui blanditiipraesnt ium voluptatum</p>
  <p class="who">CLARA VEYNE<br>Creative Strategist</p>
  <div class="stars">★★★★☆</div>
</div>
<div class="btn" style="left:481px;top:3255px;width:238px;height:51px">VIEW MORE REVIEWS</div>

<footer class="site-footer">
  <h4>Subscribe to our Newsletter</h4>
  <div class="input" style="left:164px;width:266px">Email Name</div>
  <div class="input" style="left:443px;width:266px">Email Name</div>
  <div class="btn" style="left:724px;top:86px;width:169px;height:48px">SUBSCRIBE</div>
  <div class="social" style="left:928px">Wave</div>
  <div class="social green" style="left:989px">Talk</div>
  <div class="abs" style="left:132px;top:180px;width:936px;height:1px;background:#444"></div>
  <nav class="foot-nav"><span>HOME</span><span>CRUISE LINES</span><span>SHIPS</span><span>ITINERARIES</span><span>DESTINATIONS</span><span>BLOG</span><span>ABOUT US</span><span>CONTACT</span></nav>
  <p class="copy">Copyright © 2025 Companyname. All rights reserved &nbsp;|&nbsp; Privacy Policy &nbsp;|&nbsp; Terms of Use</p>
</footer>

</body>
</html>
```